Indie author needs a minimalist book cover

I need a book cover for my latest book on personal finance and investing. The book is called, "The Quiet Harvest: Methods for Steady Savings, Careful Spending, and a Calm Future". This is volume one of a three part series on the FI/RE movement, which stands for 'Financial Independence/Retire Early'. This book is on the foundational principles of FI/RE and details the specific steps that these 'Quiet Harvest' involved in this community have done to position themselves to retire from paid work and live the life of their dreams - many only in their 20's, 30's and early 40's.

Title: The Quiet Harvest
Author: PK Brenner
Volume 1: Foundations
Book dimensions: 6"x9"

Book Blurb (for back cover):

Let's face it, no one wants to be different. But sometimes following the 'normal' crowd gets you no further than that crowd.

When it comes to money, the normal crowd is your typical consumer. Deep in debt, struggling to make ends meet, but still spending money on the newest 'thing' that just came out.

But there's another group that's been forming - right on the fringes of the personal finance world. I call them The Quiet Harvest. This book is about these superheroes of personal finance.

In it, you will learn:
• Who The Quiet Harvest are and what is this FI/RE Movement they are apart of
• What basic strategy they use to control their money
• How they became debt-free - and how you can join them
• How to use the SP/CE Lever to help you really move the needle towards financial independence
• How to diversify your income with a side-hustle and which one to choose
• The money outlier savings plan that will allow you to reach financial independence in ten years or less

This first book in The Quiet Harvest series is about building a solid foundation so you and your family can become Quiet Harvest, reach financial freedom, retire early, and live a rich life.

Target Market(s)

Individuals looking to take control of their money, reach financial independence, and retire early.

Font styles to use
Sans Serif
Other font styles liked:
• Arvo

Colors

Designer to choose colors to be used in the design.

Requirements
Must have
• A minimalist design (see examples), the title of the book, my author name, and the volume number and name (see below).
• My vision for the cover is to have a way to represent an 'outlier' in a simple, minimalistic way. I'm not set on any specific design - I'm open to what the designers come up with; I don't want to hold back anyone's creativity.
• Title: The Quiet Harvest
• Author: PK Brenner
• Volume 1: Foundations
• Book Blurb (for back cover):
• Let's face it, no one wants to be different. But sometimes following the 'normal' crowd gets you no further than that crowd.
• When it comes to money, the normal crowd is your typical consumer. Deep in debt, struggling to make ends meet, but still spending money on the newest 'thing' that just came out.
• But there's another group that's been forming - right on the fringes of the personal finance world. I call them The Quiet Harvest. This book is about these superheroes of personal finance.
• In it, you will learn:
• • Who The Quiet Harvest are and what is this FI/RE Movement they are apart of
• • What basic strategy they use to control their money
• • How they became debt-free - and how you can join them
• • How to use the SP/CE Lever to help you really move the needle towards financial independence
• • How to diversify your income with a side-hustle and which one to choose
• • The money outlier savings plan that will allow you to reach financial independence in ten years or less
• This first book in The Quiet Harvest series is about building a solid foundation so you and your family can become Quiet Harvest, reach financial freedom, retire early, and live a rich life.
Nice to have
• The subtitle - but only if it's not too crowded. Like I said before, I'm more interested in maintaining a minimalist aesthetic.
• The subtitle is: "Methods for Steady Savings, Careful Spending, And A Calm Future"
Should not have
• Too many colors or objects on the cover.

```html
<!DOCTYPE html>
<html lang="en">
<head>
<meta charset="utf-8">
<title>The Quiet Harvest — Volume 1: Foundations</title>
<link rel="stylesheet" href="https://fonts.googleapis.com/css2?family=Alfa+Slab+One&display=swap">
<style>
  :root {
    --paper: #ffffff;
    --ink: #1a1a1a;
    --accent: #e8332f;
    --flock: #c9c9c9;
    --flock-shade: #a9a9a9;
    --outlier: #e8504a;
    --outlier-shade: #d33a35;
  }
  * { margin: 0; padding: 0; box-sizing: border-box; }
  html, body { width: 800px; height: 1200px; overflow: hidden; background: var(--paper); }
  .cover {
    position: relative;
    width: 800px;
    height: 1200px;
    background: var(--paper);
    font-family: "Alfa Slab One", "Rockwell", serif;
  }
  .flock {
    position: absolute;
    left: 160px;
    top: 100px;
    width: 480px;
    display: grid;
    grid-template-columns: repeat(3, 150px);
    grid-auto-rows: 110px;
    column-gap: 15px;
    row-gap: 12px;
  }
  .sheep {
    border-radius: 46% 40% 30% 30% / 50% 50% 30% 30%;
    background: radial-gradient(ellipse at 50% 40%, var(--flock) 0%, var(--flock-shade) 100%);
  }
  .sheep--outlier {
    position: absolute;
    left: 343px;
    top: 592px;
    width: 118px;
    height: 86px;
    background: radial-gradient(ellipse at 50% 40%, var(--outlier) 0%, var(--outlier-shade) 100%);
  }
  .title-block {
    position: absolute;
    left: 222px;
    top: 840px;
    display: flex;
    align-items: flex-start;
    gap: 12px;
  }
  .volume {
    writing-mode: vertical-rl;
    transform: rotate(180deg);
    font-size: 34px;
    line-height: 1;
    letter-spacing: 2px;
    color: var(--ink);
    height: 250px;
    text-align: center;
  }
  .lines { display: flex; flex-direction: column; }
  .line {
    font-size: 54px;
    line-height: 64px;
    letter-spacing: 1px;
    text-transform: uppercase;
    white-space: nowrap;
    text-shadow: 2px 2px 0 rgba(0,0,0,0.18);
  }
  .line--title { color: var(--accent); }
  .line--author { color: var(--ink); }
  .line--series { color: var(--accent); }
</style>
</head>
<body>
  <main class="cover">
    <div class="flock" role="img" aria-label="Nine engraved black-and-white sheep standing in a neat three by three grid, all facing left">
      <div class="sheep"></div><div class="sheep"></div><div class="sheep"></div>
      <div class="sheep"></div><div class="sheep"></div><div class="sheep"></div>
      <div class="sheep"></div><div class="sheep"></div><div class="sheep"></div>
    </div>
    <div class="sheep sheep--outlier" role="img" aria-label="A single red sheep standing apart from the flock, facing right"></div>

    <section class="title-block">
      <p class="volume">Volume 1</p>
      <h1 class="lines">
        <span class="line line--title">The Quiet</span>
        <span class="line line--title">Harvest</span>
        <span class="line line--author">PK Brenner</span>
        <span class="line line--series">Foundations</span>
      </h1>
    </section>
  </main>
</body>
</html>
```